Powerpoint Presentation (urgent)

We need a powerpoint presentation to accompany our other pitch materials for a really exciting, new project.

It is a project related to gaming.

The presentation should be engaging, professionally done, and be trendy and captivating.

```html
<!DOCTYPE html>
<html lang="en">
<head>
<meta charset="utf-8">
<title>Pixelforge Pitch Deck — Slide Overview</title>
<link href="https://fonts.googleapis.com/css2?family=Rubik:wght@400;500;700&family=Roboto:wght@300;400;500&display=swap" rel="stylesheet">
<style>
:root{
  --red:#d0102b;
  --ink:#1d1d1d;
  --dark:#262626;
  --grey:#5a5a5a;
  --mute:#a9a9a9;
  --line:#d9d9d9;
  --page:#eeeeee;
  --white:#ffffff;
}
*{box-sizing:border-box;margin:0;padding:0}
html,body{width:1200px;height:1118px;overflow:hidden;background:var(--page)}
body{position:relative;font-family:"Roboto",Arial,sans-serif;color:var(--ink)}
.slide{position:absolute;width:384px;height:216px;background:var(--white);overflow:hidden;box-shadow:0 0 3px rgba(0,0,0,.18)}
.abs{position:absolute}
.s-title{position:absolute;left:18px;top:14px;font:500 17px/1.2 "Rubik",sans-serif;color:var(--ink)}
.s-title::after{content:"";position:absolute;left:0;bottom:-3px;width:22px;height:2px;background:var(--red)}
.brand{position:absolute;top:20px;right:14px;display:flex;align-items:center;gap:3px;font:700 7px/1 "Rubik",sans-serif;color:var(--red);letter-spacing:.3px}
.brand i{display:block;width:7px;height:7px;border-radius:50%;background:var(--red)}
.footer{position:absolute;left:0;bottom:0;width:100%;height:12px;background:var(--red);color:var(--white);font:400 4px/12px "Roboto",sans-serif;padding:0 6px;display:flex;justify-content:space-between}
.lead{position:absolute;font:500 7.5px/1.3 "Rubik",sans-serif;color:var(--ink)}
.hd{position:absolute;font:400 8px/1.2 "Roboto",sans-serif;color:var(--ink)}
.txt{font:300 4.4px/1.4 "Roboto",sans-serif;color:var(--mute)}
.txt p+p{margin-top:4px}
.item{position:absolute;display:flex;gap:5px;width:84px}
.item h4{font:400 6px/1.2 "Roboto",sans-serif;color:var(--ink)}
.item.red h4{color:var(--red)}
.item .txt{font-size:3.8px;line-height:1.35}
.ic{width:14px;height:14px;flex:none;color:var(--white)}
.ic circle.bg{fill:var(--ink)}
.ic.red circle.bg{fill:var(--red)}
.ic.ring circle.bg{fill:none;stroke:var(--red);stroke-width:1}
.ic.ring{color:var(--red)}
.ic.wring circle.bg{fill:none;stroke:var(--white);stroke-width:1}
.photo{position:absolute}
.num{position:absolute;left:204px;width:166px;height:30px;display:flex;align-items:center;gap:6px;padding:0 8px;color:var(--white)}
.num b{font:500 21px/1 "Rubik",sans-serif}
.num span{display:block;width:1.5px;height:20px;background:var(--white)}
.num p{font:400 4.3px/1.35 "Roboto",sans-serif}
.col{position:absolute;text-align:center;width:56px}
.col .ic{margin:0 auto 3px;display:block}
.col h4{font:400 5.5px/1.2 "Roboto",sans-serif;color:var(--ink)}
.col.red h4{color:var(--red)}
.col .txt{font-size:3.8px}
.label{font:500 3.6px/1.2 "Roboto",sans-serif;color:var(--ink)}
.dark-h{color:var(--white)}
</style>
</head>
<body>

<svg width="0" height="0" style="position:absolute" aria-hidden="true">
  <defs>
    <symbol id="g-search" viewBox="0 0 20 20"><circle cx="9" cy="9" r="3.5" fill="none" stroke="currentColor" stroke-width="1.6"/><path d="M11.6 11.6L14.5 14.5" stroke="currentColor" stroke-width="1.8" stroke-linecap="round"/></symbol>
    <symbol id="g-pen" viewBox="0 0 20 20"><path d="M6.5 13.5L13 7" stroke="currentColor" stroke-width="2.4" stroke-linecap="round"/><path d="M5.6 14.4l.8-1.8 1 1z" fill="currentColor"/></symbol>
    <symbol id="g-gear" viewBox="0 0 20 20"><circle cx="10" cy="10" r="3.8" fill="none" stroke="currentColor" stroke-width="2.6" stroke-dasharray="1.6 1.1"/><circle cx="10" cy="10" r="1.4" fill="currentColor"/></symbol>
    <symbol id="g-chart" viewBox="0 0 20 20"><path d="M7 14V11M10 14V8M13 14V6" stroke="currentColor" stroke-width="1.8"/></symbol>
    <symbol id="g-rocket" viewBox="0 0 20 20"><path d="M8 12Q10 6 14.5 5.5Q14 10 8 12Z" fill="currentColor"/><path d="M7.5 12.5L5.5 14.5" stroke="currentColor" stroke-width="1.4" stroke-linecap="round"/></symbol>
    <symbol id="g-crown" viewBox="0 0 20 20"><path d="M5.5 13.5V7.5L8 10L10 6.5L12 10L14.5 7.5V13.5Z" fill="none" stroke="currentColor" stroke-width="1.3" stroke-linejoin="round"/></symbol>
    <symbol id="g-target" viewBox="0 0 20 20"><circle cx="10" cy="10" r="4" fill="none" stroke="currentColor" stroke-width="1.4"/><circle cx="10" cy="10" r="1.6" fill="currentColor"/></symbol>
    <symbol id="g-people" viewBox="0 0 20 20"><circle cx="7.5" cy="8" r="1.8" fill="currentColor"/><circle cx="12.5" cy="8" r="1.8" fill="currentColor"/><path d="M4.5 14Q7.5 9.5 10 14M10 14Q12.5 9.5 15.5 14" fill="currentColor"/></symbol>
    <symbol id="g-lock" viewBox="0 0 20 20"><rect x="6.5" y="9.5" width="7" height="5" fill="currentColor"/><path d="M8 9.5V8a2 2 0 0 1 4 0v1.5" fill="none" stroke="currentColor" stroke-width="1.3"/></symbol>
    <symbol id="g-box" viewBox="0 0 20 20"><rect x="6" y="7" width="8" height="7" fill="none" stroke="currentColor" stroke-width="1.3"/><path d="M6 9.5H14" stroke="currentColor" stroke-width="1.1"/></symbol>
  </defs>
</svg>

<!-- 1 coffee break -->
<section class="slide" style="left:8px;top:8px;background:#141414">
  <div class="photo" role="img" aria-label="Dim photo of a coffee cup on a table" style="inset:0;background:radial-gradient(ellipse at 65% 75%,#2c2c2c 0%,#141414 60%,#0b0b0b 100%)"></div>
  <div class="brand" style="top:50px;right:26px"><i></i>PIXELFORGE</div>
  <svg class="abs" style="left:82px;top:72px;width:22px;height:22px" viewBox="0 0 20 20" aria-hidden="true"><path d="M4 9h10v3a4 4 0 0 1-4 4H8a4 4 0 0 1-4-4z" fill="#fff"/><path d="M14 10h1.5a1.6 1.6 0 0 1 0 3.2H14" fill="none" stroke="#fff" stroke-width="1.2"/><path d="M3 17.5h12" stroke="#fff" stroke-width="1.2"/><path d="M8 3q-1 1.5 0 3M11 3q-1 1.5 0 3" fill="none" stroke="#fff" stroke-width="1"/></svg>
  <div class="abs" style="left:36px;top:98px;width:120px;text-align:center;color:#fff">
    <div style="font:500 14px/1.2 'Rubik',sans-serif">COFFEE BREAK</div>
    <div style="font:300 6px/1.3 'Roboto',sans-serif">Back in 15 minutes</div>
  </div>
</section>

<!-- 2 three column description -->
<section class="slide" style="left:408px;top:8px">
  <h2 class="s-title">Three Column Description</h2>
  <div class="brand"><i></i>PIXELFORGE</div>
  <p class="lead" style="left:20px;top:56px;width:310px">This is place for your header text. Insert your text here, just replace this text with your own text</p>
  <div class="abs txt" style="left:20px;top:86px;width:100px"><p>Lorem ipsum dolor sit amet, consectetur adipiscing elit, sed do eiusmod tempor incididunt ut labore et dolore magna aliqua. Ut enim ad minim veniam, quis nostrud exercitation ullamco laboris nisi ut aliquip ex ea commodo consequat.</p><p>Duis aute irure dolor in reprehenderit in voluptate velit esse cillum dolore eu fugiat nulla pariatur excepteur occaecat.</p></div>
  <div class="abs txt" style="left:142px;top:86px;width:100px"><p>Lorem ipsum dolor sit amet, consectetur adipiscing elit, sed do eiusmod tempor incididunt ut labore et dolore magna aliqua. Ut enim ad minim veniam, quis nostrud exercitation ullamco laboris nisi ut aliquip ex ea commodo consequat.</p><p>Duis aute irure dolor in reprehenderit in voluptate velit esse cillum dolore eu fugiat nulla pariatur excepteur occaecat.</p></div>
  <div class="abs txt" style="left:264px;top:86px;width:100px"><p>Lorem ipsum dolor sit amet, consectetur adipiscing elit, sed do eiusmod tempor incididunt ut labore et dolore magna aliqua. Ut enim ad minim veniam, quis nostrud exercitation ullamco laboris nisi ut aliquip ex ea commodo consequat.</p><p>Duis aute irure dolor in reprehenderit in voluptate velit esse cillum dolore eu fugiat nulla pariatur excepteur occaecat.</p></div>
  <footer class="footer"><span>© 2017 ARCADE NORTH. All rights reserved.</span><span>20</span></footer>
</section>

<!-- 3 photo with dark panel -->
<section class="slide" style="left:808px;top:8px">
  <div class="photo" role="img" aria-label="Photo of friends jumping outdoors on a grassy field" style="left:0;top:0;width:229px;height:216px;background:linear-gradient(180deg,#8c9a86 0%,#6f7d63 45%,#5d6e44 70%,#4c5a36 100%)"></div>
  <div class="abs" style="left:229px;top:0;width:155px;height:216px;background:#1b1b1b"></div>
  <div class="brand" style="top:42px;right:44px"><i></i>PIXELFORGE</div>
  <svg class="ic wring abs" style="left:244px;top:80px;width:20px;height:20px" viewBox="0 0 20 20"><circle class="bg" cx="10" cy="10" r="9.3"/><use href="#g-rocket"/></svg>
  <svg class="ic wring abs" style="left:287px;top:80px;width:20px;height:20px" viewBox="0 0 20 20"><circle class="bg" cx="10" cy="10" r="9.3"/><use href="#g-target"/></svg>
  <svg class="ic wring abs" style="left:330px;top:80px;width:20px;height:20px" viewBox="0 0 20 20"><circle class="bg" cx="10" cy="10" r="9.3"/><use href="#g-crown"/></svg>
  <div class="abs" style="left:244px;top:112px;width:126px;height:1px;background:#555"></div>
  <h2 class="abs dark-h" style="left:244px;top:118px;font:500 15px/1.05 'Rubik',sans-serif">Your Title<br>Goes Here</h2>
  <p class="abs" style="left:244px;top:152px;width:124px;font:300 4.6px/1.35 'Roboto',sans-serif;color:#ddd">Lorem ipsum dolor sit amet, consectetur adipiscing elit, sed do eiusmod tempor incididunt ut labore et commodo consequat dolore magna aliqua.</p>
  <div class="abs" style="left:229px;top:196px;width:155px;height:20px;background:var(--red);color:#fff;font:400 5.5px/20px 'Roboto',sans-serif;text-align:center">www.pixelforge.gg</div>
</section>

<!-- 4 services + numbered -->
<section class="slide" style="left:8px;top:230px">
  <h2 class="s-title">Your Title Goes Here</h2>
  <div class="brand"><i></i>PIXELFORGE</div>
  <h3 class="hd" style="left:18px;top:48px;font-size:7px">Heading Goes Here</h3>
  <p class="abs txt" style="left:18px;top:57px;width:356px">Lorem ipsum adipiscing elit, sed do eiusmod tempor incididunt ut labore et dolore magna aliqua. Ut enim ad minim veniam, quis nostrud exercitation ullamco laboris nisi ut aliquip ex ea commodo consequat.</p>
  <div class="item" style="left:18px;top:80px;width:160px"><svg class="ic" viewBox="0 0 20 20"><circle class="bg" cx="10" cy="10" r="10"/><use href="#g-chart"/></svg><div><h4>Service Number One</h4><p class="txt">Lorem ipsum dolor sit amet, consectetur adipiscing elit, sed do eiusmod tempor incididunt ut labore et dolore magna aliqua.</p></div></div>
  <div class="item red" style="left:18px;top:116px;width:160px"><svg class="ic red" viewBox="0 0 20 20"><circle class="bg" cx="10" cy="10" r="10"/><use href="#g-rocket"/></svg><div><h4>Service Number Two</h4><p class="txt">Lorem ipsum dolor sit amet, consectetur adipiscing elit, sed do eiusmod tempor incididunt ut labore et dolore magna aliqua.</p></div></div>
  <div class="item" style="left:18px;top:154px;width:160px"><svg class="ic" viewBox="0 0 20 20"><circle class="bg" cx="10" cy="10" r="10"/><use href="#g-search"/></svg><div><h4>Service Number Three</h4><p class="txt">Lorem ipsum dolor sit amet, consectetur adipiscing elit, sed do eiusmod tempor incididunt ut labore et dolore magna aliqua.</p></div></div>
  <div class="num" style="top:76px;background:#151515"><b>1</b><span></span><p>Lorem ipsum dolor sit amet, consectetur adipiscing elit, sed do eiusmod tempor incididunt ut labore et dolore magna aliqua.</p></div>
  <div class="num" style="top:113px;background:var(--red)"><b>2</b><span></span><p>Lorem ipsum dolor sit amet, consectetur adipiscing elit, sed do eiusmod tempor incididunt ut labore et dolore magna aliqua.</p></div>
  <div class="num" style="top:150px;background:#333"><b>3</b><span></span><p>Lorem ipsum dolor sit amet, consectetur adipiscing elit, sed do eiusmod tempor incididunt ut labore et dolore magna aliqua.</p></div>
  <footer class="footer"><span>© 2017 ARCADE NORTH. All rights reserved.</span><span>22</span></footer>
</section>

<!-- 5 four bullets -->
<section class="slide" style="left:408px;top:230px">
  <h2 class="s-title">Four Bullets with Paragraph</h2>
  <div class="brand"><i></i>PIXELFORGE</div>
  <div class="item" style="left:22px;top:72px"><svg class="ic" viewBox="0 0 20 20"><circle class="bg" cx="10" cy="10" r="10"/><use href="#g-search"/></svg><div><h4>Your Text Here</h4><p class="txt">Lorem ipsum dolor sit amet, consectetur adipiscing elit, sed do eiusmod</p></div></div>
  <div class="item" style="left:108px;top:72px"><svg class="ic" viewBox="0 0 20 20"><circle class="bg" cx="10" cy="10" r="10"/><use href="#g-pen"/></svg><div><h4>Your Text Here</h4><p class="txt">Lorem ipsum dolor sit amet, consectetur adipiscing elit, sed do eiusmod</p></div></div>
  <div class="item" style="left:22px;top:134px"><svg class="ic" viewBox="0 0 20 20"><circle class="bg" cx="10" cy="10" r="10"/><use href="#g-gear"/></svg><div><h4>Your Text Here</h4><p class="txt">Lorem ipsum dolor sit amet, consectetur adipiscing elit, sed do eiusmod</p></div></div>
  <div class="item" style="left:108px;top:134px"><svg class="ic" viewBox="0 0 20 20"><circle class="bg" cx="10" cy="10" r="10"/><use href="#g-rocket"/></svg><div><h4>Your Text Here</h4><p class="txt">Lorem ipsum dolor sit amet, consectetur adipiscing elit, sed do eiusmod</p></div></div>
  <h3 class="hd" style="left:210px;top:70px;font-size:8.5px">Heading Goes Here</h3>
  <div class="abs txt" style="left:210px;top:84px;width:158px;font-size:5px"><p>Lorem ipsum dolor sit amet, consectetur adipiscing elit, sed do eiusmod tempor incididunt ut labore et commodo consequat dolore magna aliqua.</p><p>Duis aute irure dolor in reprehenderit in voluptate velit esse cillum dolore eu fugiat nulla pariatur.</p><p>Ut enim minim veniam, quis nostrud exercitation ullamco laboris nisi ut aliquip ex ea commodo consequat.</p></div>
  <footer class="footer"><span>© 2017 ARCADE NORTH. All rights reserved.</span><span>23</span></footer>
</section>

<!-- 6 your title with photo -->
<section class="slide" style="left:808px;top:230px">
  <h2 class="s-title">Your Title</h2>
  <div class="brand"><i></i>PIXELFORGE</div>
  <h3 class="hd" style="left:16px;top:66px;font-size:8.5px">Heading Goes Here</h3>
  <div class="abs txt" style="left:16px;top:80px;width:100px"><p>Lorem ipsum dolor sit amet, consectetur adipiscing elit, sed do eiusmod tempor incididunt ut labore et commodo consequat dolore magna aliqua.</p><p>Duis aute irure dolor in reprehenderit in voluptate velit esse cillum dolore eu fugiat nulla pariatur.</p><p>Ut enim minim veniam, quis nostrud exercitation ullamco laboris nisi ut aliquip ex ea commodo consequat.</p></div>
  <div class="photo" role="img" aria-label="Photo of two children looking at a tablet" style="left:122px;top:0;width:140px;height:204px;background:linear-gradient(160deg,#c9d0c2 0%,#a9b39a 35%,#c49a7c 65%,#8f7e6c 100%)"></div>
  <div class="item" style="left:272px;top:66px;width:104px"><svg class="ic" viewBox="0 0 20 20"><circle class="bg" cx="10" cy="10" r="10"/><use href="#g-search"/></svg><div><h4>Your Text Here</h4><p class="txt">Lorem ipsum dolor sit amet, adipiscing elit, sed do eiusmod</p></div></div>
  <div class="item" style="left:272px;top:98px;width:104px"><svg class="ic" viewBox="0 0 20 20"><circle class="bg" cx="10" cy="10" r="10"/><use href="#g-pen"/></svg><div><h4>Your Text Here</h4><p class="txt">Lorem ipsum dolor sit amet, adipiscing elit, sed do eiusmod</p></div></div>
  <div class="item" style="left:272px;top:129px;width:104px"><svg class="ic" viewBox="0 0 20 20"><circle class="bg" cx="10" cy="10" r="10"/><use href="#g-rocket"/></svg><div><h4>Your Text Here</h4><p class="txt">Lorem ipsum dolor sit amet, adipiscing elit, sed do eiusmod</p></div></div>
  <div class="item" style="left:272px;top:160px;width:104px"><svg class="ic" viewBox="0 0 20 20"><circle class="bg" cx="10" cy="10" r="10"/><use href="#g-gear"/></svg><div><h4>Your Text Here</h4><p class="txt">Lorem ipsum dolor sit amet, adipiscing elit, sed do eiusmod</p></div></div>
  <footer class="footer"><span>© 2017 ARCADE NORTH. All rights reserved.</span><span>24</span></footer>
</section>

<!-- 7 text & bullet -->
<section class="slide" style="left:8px;top:452px">
  <h2 class="s-title">Text &amp; Bullet Area</h2>
  <div class="brand"><i></i>PIXELFORGE</div>
  <h3 class="hd" style="left:20px;top:62px;font-size:8.5px">Heading Goes Here</h3>
  <div class="abs txt" style="left:20px;top:77px;width:98px"><p>Lorem ipsum dolor sit amet, consectetur adipiscing elit, sed do eiusmod tempor incididunt ut labore et commodo consequat dolore magna aliqua.</p><p>Duis aute irure dolor in reprehenderit in voluptate velit esse cillum dolore eu fugiat nulla pariatur.</p><p>Ut enim minim veniam, quis nostrud exercitation ullamco laboris nisi ut aliquip ex ea commodo consequat.</p></div>
  <div class="item" style="left:142px;top:62px;width:112px"><svg class="ic" viewBox="0 0 20 20"><circle class="bg" cx="10" cy="10" r="10"/><use href="#g-crown"/></svg><div><h4>Your Text Here</h4><p class="txt">Lorem ipsum dolor sit amet, consectetur adipiscing elit, sed do eiusmod.</p></div></div>
  <div class="item red" style="left:142px;top:94px;width:112px"><svg class="ic red" viewBox="0 0 20 20"><circle class="bg" cx="10" cy="10" r="10"/><use href="#g-chart"/></svg><div><h4>Your Text Here</h4><p class="txt">Lorem ipsum dolor sit amet, consectetur adipiscing elit, sed do eiusmod.</p></div></div>
  <div class="item" style="left:142px;top:125px;width:112px"><svg class="ic" viewBox="0 0 20 20"><circle class="bg" cx="10" cy="10" r="10"/><use href="#g-people"/></svg><div><h4>Your Text Here</h4><p class="txt">Lorem ipsum dolor sit amet, consectetur adipiscing elit, sed do eiusmod.</p></div></div>
  <div class="item red" style="left:142px;top:156px;width:112px"><svg class="ic red" viewBox="0 0 20 20"><circle class="bg" cx="10" cy="10" r="10"/><use href="#g-target"/></svg><div><h4>Your Text Here</h4><p class="txt">Lorem ipsum dolor sit amet, consectetur adipiscing elit, sed do eiusmod.</p></div></div>
  <div class="item red" style="left:264px;top:62px;width:112px"><svg class="ic red" viewBox="0 0 20 20"><circle class="bg" cx="10" cy="10" r="10"/><use href="#g-search"/></svg><div><h4>Your Text Here</h4><p class="txt">Lorem ipsum dolor sit amet, consectetur adipiscing elit, sed do eiusmod.</p></div></div>
  <div class="item" style="left:264px;top:94px;width:112px"><svg class="ic" viewBox="0 0 20 20"><circle class="bg" cx="10" cy="10" r="10"/><use href="#g-pen"/></svg><div><h4>Your Text Here</h4><p class="txt">Lorem ipsum dolor sit amet, consectetur adipiscing elit, sed do eiusmod.</p></div></div>
  <div class="item red" style="left:264px;top:125px;width:112px"><svg class="ic red" viewBox="0 0 20 20"><circle class="bg" cx="10" cy="10" r="10"/><use href="#g-rocket"/></svg><div><h4>Your Text Here</h4><p class="txt">Lorem ipsum dolor sit amet, consectetur adipiscing elit, sed do eiusmod.</p></div></div>
  <div class="item" style="left:264px;top:156px;width:112px"><svg class="ic" viewBox="0 0 20 20"><circle class="bg" cx="10" cy="10" r="10"/><use href="#g-gear"/></svg><div><h4>Your Text Here</h4><p class="txt">Lorem ipsum dolor sit amet, consectetur adipiscing elit, sed do eiusmod.</p></div></div>
  <footer class="footer"><span>© 2017 ARCADE NORTH. All rights reserved.</span><span>25</span></footer>
</section>

<!-- 8 divider -->
<section class="slide" style="left:408px;top:452px;background:#222">
  <div class="photo" role="img" aria-label="Dark photo of a group of friends sitting on a bench" style="inset:0;background:linear-gradient(180deg,#3a3a3a 0%,#2b2b2b 55%,#1c1c1c 100%)"></div>
  <div class="brand" style="top:62px;right:20px"><i></i>PIXELFORGE</div>
  <div class="abs" style="left:6px;top:112px;width:220px;text-align:center;color:#fff">
    <div style="font:400 6px/1.2 'Roboto',sans-serif;padding-right:60px">Divider Page</div>
    <div style="font:500 16.5px/1.2 'Rubik',sans-serif">Your Title Goes Here</div>
    <div style="font:300 8.5px/1.2 'Roboto',sans-serif">Your Subtitle Here</div>
  </div>
</section>

<!-- 9 paragraph with three bullet -->
<section class="slide" style="left:808px;top:452px">
  <h2 class="s-title">Paragraph With Three Bullet</h2>
  <div class="brand"><i></i>PIXELFORGE</div>
  <p class="lead" style="left:18px;top:56px;width:320px">This is place for your header text. Insert your text here, just replace this text with your own text</p>
  <div class="abs txt" style="left:18px;top:98px;width:120px"><p>Lorem ipsum dolor sit amet, consectetur adipiscing elit, sed do eiusmod tempor incididunt ut labore et dolore magna aliqua. Ut enim minim veniam, quis nostrud exercitation ullamco laboris nisi ut aliquip ex ea commodo consequat.</p><p>Duis aute irure dolor in reprehenderit in voluptate velit esse cillum dolore eu fugiat nulla pariatur excepteur occaecat.</p></div>
  <div class="col red" style="left:152px;top:86px;width:60px"><svg class="ic ring" style="width:18px;height:18px" viewBox="0 0 20 20"><circle class="bg" cx="10" cy="10" r="9.4"/><use href="#g-target"/></svg><h4>Your Text Here</h4><p class="txt">Lorem ipsum dolor sit amet, consectetur adipiscing elit, sed do eiusmod tempor incididunt ut labore et dolore aliqua.</p><p class="txt" style="margin-top:4px">Ut enim minim veniam, quis nostrud exercitation ullamco laboris commodo consequat.</p></div>
  <div class="col red" style="left:228px;top:86px;width:60px"><svg class="ic ring" style="width:18px;height:18px" viewBox="0 0 20 20"><circle class="bg" cx="10" cy="10" r="9.4"/><use href="#g-crown"/></svg><h4>Your Text Here</h4><p class="txt">Lorem ipsum dolor sit amet, consectetur adipiscing elit, sed do eiusmod tempor incididunt ut labore et dolore aliqua.</p><p class="txt" style="margin-top:4px">Ut enim minim veniam, quis nostrud exercitation ullamco laboris commodo consequat.</p></div>
  <div class="col red" style="left:306px;top:86px;width:60px"><svg class="ic ring" style="width:18px;height:18px" viewBox="0 0 20 20"><circle class="bg" cx="10" cy="10" r="9.4"/><use href="#g-rocket"/></svg><h4>Your Text Here</h4><p class="txt">Lorem ipsum dolor sit amet, consectetur adipiscing elit, sed do eiusmod tempor incididunt ut labore et dolore aliqua.</p><p class="txt" style="margin-top:4px">Ut enim minim veniam, quis nostrud exercitation ullamco laboris commodo consequat.</p></div>
  <footer class="footer"><span>© 2017 ARCADE NORTH. All rights reserved.</span><span>27</span></footer>
</section>

<!-- 10 global experience -->
<section class="slide" style="left:8px;top:674px">
  <h2 class="s-title">Global Experience</h2>
  <div class="brand"><i></i>PIXELFORGE</div>
  <div class="photo" role="img" aria-label="Dotted world map with location markers" style="left:98px;top:38px;width:262px;height:140px;background:radial-gradient(ellipse at center,#e4e4e4 0%,#eeeeee 60%,#fafafa 100%)"></div>
  <div class="abs" style="left:18px;top:166px;display:flex;align-items:center;gap:5px"><i style="display:block;width:12px;height:12px;border-radius:50%;background:#111"></i><span style="font:400 7px 'Roboto',sans-serif">Heading Goes Here</span></div>
  <p class="abs txt" style="left:18px;top:181px;width:230px">Lorem ipsum dolor sit amet, consectetur adipiscing elit, sed do eiusmod tempor incididunt ut labore et dolore magna aliqua</p>
  <footer class="footer"><span>© 2017 ARCADE NORTH. All rights reserved.</span><span>28</span></footer>
</section>

<!-- 11 multiple column -->
<section class="slide" style="left:408px;top:674px">
  <h2 class="s-title">Multiple Column Area</h2>
  <div class="brand"><i></i>PIXELFORGE</div>
  <div class="col" style="left:22px;top:56px"><svg class="ic" viewBox="0 0 20 20"><circle class="bg" cx="10" cy="10" r="10"/><use href="#g-gear"/></svg><h4>Your Text Here</h4><p class="txt">Lorem ipsum consectetur adipiscing elit</p></div>
  <div class="col red" style="left:92px;top:56px"><svg class="ic red" viewBox="0 0 20 20"><circle class="bg" cx="10" cy="10" r="10"/><use href="#g-rocket"/></svg><h4>Your Text Here</h4><p class="txt">Lorem ipsum consectetur adipiscing elit</p></div>
  <div class="col" style="left:162px;top:56px"><svg class="ic" viewBox="0 0 20 20"><circle class="bg" cx="10" cy="10" r="10"/><use href="#g-search"/></svg><h4>Your Text Here</h4><p class="txt">Lorem ipsum consectetur adipiscing elit</p></div>
  <div class="col red" style="left:233px;top:56px"><svg class="ic red" viewBox="0 0 20 20"><circle class="bg" cx="10" cy="10" r="10"/><use href="#g-pen"/></svg><h4>Your Text Here</h4><p class="txt">Lorem ipsum consectetur adipiscing elit</p></div>
  <div class="col" style="left:304px;top:56px"><svg class="ic" viewBox="0 0 20 20"><circle class="bg" cx="10" cy="10" r="10"/><use href="#g-chart"/></svg><h4>Your Text Here</h4><p class="txt">Lorem ipsum consectetur adipiscing elit</p></div>
  <div class="abs" style="left:28px;top:114px;width:330px;height:1px;background:var(--red)"></div>
  <h3 class="hd" style="left:28px;top:125px">Heading Goes Here</h3>
  <div class="abs txt" style="left:28px;top:137px;width:170px"><p>Lorem ipsum dolor sit amet, consectetur adipiscing elit, sed do eiusmod tempor incididunt ut labore et commodo consequat dolore magna aliqua.</p><p>Duis aute irure dolor in reprehenderit in voluptate velit esse cillum dolore eu fugiat nulla pariatur.</p></div>
  <h3 class="hd" style="left:208px;top:125px">Heading Goes Here</h3>
  <div class="abs txt" style="left:208px;top:137px;width:160px"><p>Lorem ipsum dolor sit amet, consectetur adipiscing elit, sed do eiusmod tempor incididunt ut labore et commodo consequat dolore magna aliqua.</p><p>Duis aute irure dolor in reprehenderit in voluptate velit esse cillum dolore eu fugiat nulla pariatur.</p></div>
  <footer class="footer"><span>© 2017 ARCADE NORTH. All rights reserved.</span><span>29</span></footer>
</section>

<!-- 12 four ring charts -->
<section class="slide" style="left:808px;top:674px">
  <h2 class="s-title">Your Pie Chart Area</h2>
  <div class="brand"><i></i>PIXELFORGE</div>
  <svg class="abs" style="left:0;top:0;width:384px;height:216px" viewBox="0 0 384 216" aria-label="Four ring charts showing 20, 50, 70 and 30 percent">
    <g fill="none" stroke-width="5" font-family="Rubik,sans-serif" font-size="9" text-anchor="middle">
      <circle cx="60" cy="100" r="18" stroke="#d8d8d8"/>
      <circle cx="60" cy="100" r="18" stroke="#1d1d1d" pathLength="100" stroke-dasharray="20 80" transform="rotate(-90 60 100)"/>
      <text x="60" y="103" fill="#1d1d1d" stroke="none">20%</text>
      <circle cx="147" cy="100" r="18" stroke="#d8d8d8"/>
      <circle cx="147" cy="100" r="18" stroke="#d0102b" pathLength="100" stroke-dasharray="50 50" transform="rotate(-90 147 100)"/>
      <text x="147" y="103" fill="#d0102b" stroke="none">50%</text>
      <circle cx="237" cy="100" r="18" stroke="#d8d8d8"/>
      <circle cx="237" cy="100" r="18" stroke="#1d1d1d" pathLength="100" stroke-dasharray="70 30" transform="rotate(-90 237 100)"/>
      <text x="237" y="103" fill="#1d1d1d" stroke="none">70%</text>
      <circle cx="325" cy="100" r="18" stroke="#d8d8d8"/>
      <circle cx="325" cy="100" r="18" stroke="#8a8a8a" pathLength="100" stroke-dasharray="30 70" transform="rotate(-90 325 100)"/>
      <text x="325" y="103" fill="#8a8a8a" stroke="none">30%</text>
    </g>
  </svg>
  <div class="col" style="left:30px;top:126px;width:60px"><p class="label">Subtitle in this area</p><p class="txt" style="font-size:3.7px">Lorem ipsum dolor sit amet, consectetur adipiscing elit integer mollis vehicula ligula ut faucibus vestibulum</p></div>
  <div class="col" style="left:117px;top:126px;width:60px"><p class="label" style="color:var(--red)">Subtitle in this area</p><p class="txt" style="font-size:3.7px">Lorem ipsum dolor sit amet, consectetur adipiscing elit integer mollis vehicula ligula ut faucibus vestibulum</p></div>
  <div class="col" style="left:207px;top:126px;width:60px"><p class="label">Subtitle in this area</p><p class="txt" style="font-size:3.7px">Lorem ipsum dolor sit amet, consectetur adipiscing elit integer mollis vehicula ligula ut faucibus vestibulum</p></div>
  <div class="col" style="left:295px;top:126px;width:60px"><p class="label">Subtitle in this area</p><p class="txt" style="font-size:3.7px">Lorem ipsum dolor sit amet, consectetur adipiscing elit integer mollis vehicula ligula ut faucibus vestibulum</p></div>
  <footer class="footer"><span>© 2017 ARCADE NORTH. All rights reserved.</span><span>30</span></footer>
</section>

<!-- 13 donut with icons -->
<section class="slide" style="left:8px;top:896px">
  <h2 class="s-title">Your Pie Chart Area</h2>
  <div class="brand"><i></i>PIXELFORGE</div>
  <svg class="abs" style="left:148px;top:66px;width:90px;height:90px" viewBox="0 0 90 90" aria-label="Donut chart with four segments">
    <g fill="none" stroke-width="20" transform="rotate(-90 45 45)">
      <circle cx="45" cy="45" r="32" stroke="#d0102b" pathLength="125" stroke-dasharray="35 90"/>
      <circle cx="45" cy="45" r="32" stroke="#555" pathLength="125" stroke-dasharray="40 85" stroke-dashoffset="-35"/>
      <circle cx="45" cy="45" r="32" stroke="#2a2a2a" pathLength="125" stroke-dasharray="30 95" stroke-dashoffset="-75"/>
      <circle cx="45" cy="45" r="32" stroke="#111" pathLength="125" stroke-dasharray="20 105" stroke-dashoffset="-105"/>
    </g>
    <g fill="#fff" font-family="Rubik,sans-serif" font-size="7.5" font-weight="500" text-anchor="middle">
      <text x="25" y="28">20%</text><text x="68" y="37">35%</text><text x="55" y="72">40%</text><text x="17" y="62">30%</text>
    </g>
  </svg>
  <div class="abs" style="left:60px;top:60px;width:64px;text-align:right"><p class="label">Secure</p><p class="txt" style="font-size:3.7px">Nullam eu tempor purus. Nunc a leo magna, sit amet consequat risus</p></div>
  <svg class="ic abs" style="left:128px;top:64px;width:26px;height:26px" viewBox="0 0 20 20"><circle class="bg" cx="10" cy="10" r="10"/><use href="#g-lock"/></svg>
  <svg class="ic red abs" style="left:250px;top:64px;width:26px;height:26px" viewBox="0 0 20 20"><circle class="bg" cx="10" cy="10" r="10"/><use href="#g-target"/></svg>
  <div class="abs" style="left:282px;top:60px;width:64px"><p class="label" style="color:var(--red)">Well Organized</p><p class="txt" style="font-size:3.7px">Nullam eu tempor purus. Nunc a leo magna, sit amet consequat risus</p></div>
  <div class="abs" style="left:60px;top:132px;width:64px;text-align:right"><p class="label">Good Package</p><p class="txt" style="font-size:3.7px">Nullam eu tempor purus. Nunc a leo magna, sit amet consequat risus</p></div>
  <svg class="ic abs" style="left:128px;top:130px;width:26px;height:26px" viewBox="0 0 20 20"><circle class="bg" cx="10" cy="10" r="10" style="fill:#444"/><use href="#g-box"/></svg>
  <svg class="ic abs" style="left:250px;top:130px;width:26px;height:26px" viewBox="0 0 20 20"><circle class="bg" cx="10" cy="10" r="10" style="fill:#777"/><use href="#g-box"/></svg>
  <div class="abs" style="left:282px;top:132px;width:64px"><p class="label">Publication</p><p class="txt" style="font-size:3.7px">Nullam eu tempor purus. Nunc a leo magna, sit amet consequat risus</p></div>
  <p class="abs txt" style="left:70px;top:184px;width:250px;text-align:center;font-size:3.8px">Lorem ipsum dolor sit amet, consectetur adipiscing elit. Sed et consectetur lacus. Sed sit amet nulla vel dolor gravida bibendum. Nunc odio massa, sodales et consectetur a, iaculis eget sapien.</p>
  <footer class="footer"><span>© 2017 ARCADE NORTH. All rights reserved.</span><span>31</span></footer>
</section>

<!-- 14 tilted pie -->
<section class="slide" style="left:408px;top:896px">
  <h2 class="s-title">Your Pie Chart Area</h2>
  <div class="brand"><i></i>PIXELFORGE</div>
  <svg class="abs" style="left:50px;top:50px;width:140px;height:90px" viewBox="0 0 140 90" aria-label="Tilted pie chart with three sales segments">
    <path d="M2 38v12a68 34 0 0 0 136 0V38" fill="#141414"/>
    <ellipse cx="70" cy="38" rx="68" ry="34" fill="#262626"/>
    <path d="M70 38L8 52A68 34 0 0 1 20 16Z" fill="#d0102b"/>
    <path d="M8 52v12L-1 50Z" fill="#8d0a1e"/>
    <path d="M70 38L70 4" stroke="#fff" stroke-width="2"/>
    <path d="M70 38L8 52" stroke="#fff" stroke-width="1.5"/>
  </svg>
  <div class="abs" style="left:110px;top:140px;display:flex;gap:6px;font:300 3.5px 'Roboto',sans-serif;color:var(--mute)"><span>■ Sales A</span><span>■ Sales B</span><span>■ Sales C</span></div>
  <div class="item" style="left:246px;top:68px;width:130px"><svg class="ic" style="width:12px;height:12px" viewBox="0 0 20 20"><circle class="bg" cx="10" cy="10" r="10"/><use href="#g-chart"/></svg><div><h4>Your Text Here</h4><p class="txt" style="font-size:4.4px">Lorem ipsum dolor sit amet.</p></div></div>
  <div class="item red" style="left:246px;top:95px;width:130px"><svg class="ic red" style="width:12px;height:12px" viewBox="0 0 20 20"><circle class="bg" cx="10" cy="10" r="10"/><use href="#g-rocket"/></svg><div><h4>Your Text Here</h4><p class="txt" style="font-size:4.4px">Lorem ipsum dolor sit amet.</p></div></div>
  <div class="item" style="left:246px;top:122px;width:130px"><svg class="ic" style="width:12px;height:12px" viewBox="0 0 20 20"><circle class="bg" cx="10" cy="10" r="10" style="fill:#555"/><use href="#g-gear"/></svg><div><h4>Your Text Here</h4><p class="txt" style="font-size:4.4px">Lorem ipsum dolor sit amet.</p></div></div>
  <div class="abs" style="left:26px;top:160px;display:flex;align-items:center;gap:3px;font:500 16px/1 'Rubik',sans-serif"><svg width="11" height="10" viewBox="0 0 11 10" aria-hidden="true"><path d="M5.5 0L11 10H0Z" fill="#d0102b"/></svg>54%</div>
  <h3 class="hd" style="left:79px;top:156px;font-size:7px">Heading Goes Here</h3>
  <p class="abs txt" style="left:79px;top:165px;width:220px;font-size:4.8px">Lorem ipsum adipiscing elit, sed do eiusmod tempor incididunt ut labore et dolore magna aliqua. Ut enim minim veniam, quis nostrud exercitation ullamco laboris nisi ut aliquip ex ea commodo consequat.</p>
  <footer class="footer"><span>© 2017 ARCADE NORTH. All rights reserved.</span><span>32</span></footer>
</section>

<!-- 15 line charts -->
<section class="slide" style="left:808px;top:896px">
  <h2 class="s-title">Your Line Chart Area</h2>
  <div class="brand"><i></i>PIXELFORGE</div>
  <svg class="abs" style="left:0;top:0;width:384px;height:216px" viewBox="0 0 384 216" aria-label="Two line charts comparing two series">
    <g font-family="Roboto,sans-serif" font-size="6" fill="#333" text-anchor="middle">
      <text x="97" y="72">Chart Title</text><text x="277" y="72">Chart Title</text>
    </g>
    <g font-family="Roboto,sans-serif" font-size="3.5" fill="#aaa" text-anchor="end">
      <text x="32" y="82">70</text><text x="32" y="92">60</text><text x="32" y="102">50</text><text x="32" y="112">40</text><text x="32" y="122">30</text><text x="32" y="132">20</text><text x="32" y="142">10</text><text x="32" y="152">0</text>
      <text x="212" y="82">70</text><text x="212" y="92">60</text><text x="212" y="102">50</text><text x="212" y="112">40</text><text x="212" y="122">30</text><text x="212" y="132">20</text><text x="212" y="142">10</text><text x="212" y="152">0</text>
    </g>
    <g font-family="Roboto,sans-serif" font-size="4" fill="#999" text-anchor="middle">
      <text x="50" y="158">ab</text><text x="76" y="158">bc</text><text x="102" y="158">cd</text><text x="128" y="158">ef</text><text x="154" y="158">fg</text>
      <text x="230" y="158">ab</text><text x="256" y="158">bc</text><text x="282" y="158">cd</text><text x="308" y="158">ef</text><text x="334" y="158">fg</text>
    </g>
    <path d="M38 151H166M218 151H346" stroke="#ddd" stroke-width=".6"/>
    <polyline points="42,140 64,92 84,120 106,104 128,124 152,100" fill="none" stroke="#1d1d1d" stroke-width="1.3"/>
    <polyline points="42,124 60,112 82,146 104,92 128,108 152,126" fill="none" stroke="#d0102b" stroke-width="1.3"/>
    <g font-family="Roboto,sans-serif" font-size="5" fill="#1d1d1d"><text x="38" y="138">10</text><text x="60" y="90">60</text><text x="86" y="118">30</text><text x="104" y="116">40</text><text x="150" y="98">50</text></g>
    <g font-family="Roboto,sans-serif" font-size="5" fill="#d0102b"><text x="34" y="124">40</text><text x="54" y="110">20</text><text x="84" y="144">30</text><text x="100" y="90">60</text><text x="150" y="133">30</text></g>
    <polyline points="222,140 244,108 262,126 284,104 306,124 328,98 346,114" fill="none" stroke="#1d1d1d" stroke-width="1.3"/>
    <polyline points="222,128 244,98 262,134 286,110 306,112 330,94 346,120" fill="none" stroke="#d0102b" stroke-width="1.3"/>
  </svg>
  <div class="abs txt" style="left:38px;top:166px;width:140px;font-size:3.8px"><span style="color:#333;font-weight:400;font-size:4.6px">Lorem ipsum dolor sit amet,</span> consectetur adipiscing elit sed diam nonummy nibh euismod tincidunt ut laoreet dolore magna aliquam erat volutpat.</div>
  <div class="abs txt" style="left:218px;top:166px;width:140px;font-size:3.8px"><span style="color:#333;font-weight:400;font-size:4.6px">Lorem ipsum dolor sit amet,</span> consectetur adipiscing elit sed diam nonummy nibh euismod tincidunt ut laoreet dolore magna aliquam erat volutpat.</div>
  <footer class="footer"><span>© 2017 ARCADE NORTH. All rights reserved.</span><span>33</span></footer>
</section>

</body>
</html>
```